Business Card for boutique psychology business

Business card for boutique psychology practice in Melbourne. I want them to be relatively simply with the logo and backing colour taking up the front side. Then, text on the back, with my name; professional title (Clinical Psychologist); website - torvinpsychology.com.au; email: hello@torvinpsychology.com.au; insta: @torvin.psychology.emdr
Back should also have the words: Connect. Integrate. Evolve
Fonts used for logo are: Mikea Demo and Gotham Medium. Use something for back text that will compliment these.
Brand colours uploaded below. I'd like to see options in both olive and blush.

```html
<!DOCTYPE html>
<html lang="en">
<head>
<meta charset="utf-8">
<title>Torvin Psychology Business Card</title>
<link href="https://fonts.googleapis.com/css2?family=Montserrat:wght@500&family=Josefin+Sans:wght@300;400&family=EB+Garamond:wght@400&display=swap" rel="stylesheet">
<style>
  :root {
    --backdrop: #1c1c1c;
    --olive: #434730;
    --blush: #e8cdbe;
    --card-w: 880px;
    --card-h: 503px;
  }
  html, body {
    margin: 0;
    width: 1200px;
    height: 1200px;
    overflow: hidden;
    background: var(--backdrop);
  }
  .canvas {
    position: relative;
    width: 1200px;
    height: 1200px;
  }
  .card {
    position: absolute;
    left: 160px;
    width: var(--card-w);
    height: var(--card-h);
    overflow: hidden;
  }
  .card--front { top: 70px; background: var(--blush); }
  .card--back  { top: 627px; background: var(--olive); }

  .band { position: absolute; left: 0; width: 100%; }
  .band--stripe { top: 330px; height: 22px; }
  .band--main { top: 372px; height: 68px; display: flex; align-items: center; justify-content: center; }
  .card--front .band { background: var(--olive); }
  .card--back .band { background: var(--blush); }

  .wordmark {
    position: absolute;
    top: 70px;
    left: 0;
    width: 100%;
    text-align: center;
    font-family: "Montserrat", sans-serif;
    font-weight: 500;
    color: var(--olive);
  }
  .wordmark__name {
    display: block;
    font-size: 124px;
    line-height: 1;
    letter-spacing: 2px;
  }
  .wordmark__sub {
    display: block;
    margin-top: 8px;
    font-size: 30px;
    letter-spacing: 1px;
  }

  .tagline {
    font-family: "Josefin Sans", sans-serif;
    font-weight: 400;
    font-size: 22px;
    letter-spacing: 4px;
    color: var(--blush);
  }
  .tagline__sep { margin: 0 16px; }

  .identity {
    position: absolute;
    top: 150px;
    left: 90px;
    width: 300px;
    color: var(--blush);
  }
  .identity__name {
    font-family: "Josefin Sans", sans-serif;
    font-weight: 300;
    font-size: 36px;
    letter-spacing: 3px;
    line-height: 1;
  }
  .identity__title {
    margin-top: 8px;
    font-family: "EB Garamond", serif;
    font-size: 26px;
    letter-spacing: 0.5px;
  }
  .divider {
    position: absolute;
    top: 140px;
    left: 395px;
    width: 2px;
    height: 110px;
    background: var(--blush);
  }
  .contacts {
    position: absolute;
    top: 168px;
    left: 425px;
    margin: 0;
    padding: 0;
    list-style: none;
    font-family: "EB Garamond", serif;
    font-size: 26px;
    color: var(--blush);
  }
  .contacts__item { display: flex; align-items: center; gap: 14px; line-height: 1.35; }
  .contacts__icon { width: 20px; height: 16px; flex: none; }

  .website {
    font-family: "EB Garamond", serif;
    font-size: 24px;
    letter-spacing: 6px;
    color: var(--olive);
  }
</style>
</head>
<body>
<main class="canvas">
  <section class="card card--front" aria-label="Card front">
    <div class="wordmark">
      <span class="wordmark__name">torvin</span>
      <span class="wordmark__sub">psychology + EMDR</span>
    </div>
    <div class="band band--stripe"></div>
    <div class="band band--main">
      <p class="tagline">CONNECT<span class="tagline__sep">|</span>INTEGRATE<span class="tagline__sep">|</span>EVOLVE</p>
    </div>
  </section>

  <section class="card card--back" aria-label="Card back">
    <div class="identity">
      <div class="identity__name">MAREN HOLT</div>
      <div class="identity__title">Clinical Psychologist</div>
    </div>
    <div class="divider"></div>
    <ul class="contacts">
      <li class="contacts__item">
        <svg class="contacts__icon" viewBox="0 0 20 16" aria-hidden="true">
          <rect x="1" y="1" width="18" height="14" fill="none" stroke="#e8cdbe" stroke-width="2"/>
          <polyline points="1,1 10,9 19,1" fill="none" stroke="#e8cdbe" stroke-width="2"/>
        </svg>
        hello@torvinpsychology.com.au
      </li>
      <li class="contacts__item">
        <svg class="contacts__icon" viewBox="0 0 20 16" aria-hidden="true">
          <circle cx="10" cy="8" r="7" fill="#e8cdbe"/>
        </svg>
        @torvin.psychology.emdr
      </li>
    </ul>
    <div class="band band--stripe"></div>
    <div class="band band--main">
      <p class="website">www.torvinpsychology.com.au</p>
    </div>
  </section>
</main>
</body>
</html>
```